New web page, 2 companies on the one page

A new web page for an engineering consultancy and maintenance management company

Corrick & Associates is the parent company covering the design and consultancy
Trivolt Engineering is the Maintenance and Reliability company

Target Market(s)

Food & Beverage, ingredients Manufacturing
engineering managers

Coding

Coded - Design and coding required

Number of Pages Required

1 page

Font styles to use
Other font styles liked:
• Roboto

Colors
1861ab
85acd3
d0dfed
cee9f5

```html
<!DOCTYPE html>
<html lang="en">
<head>
<meta charset="utf-8">
<title>Trivolt Engineering – Manufacturing Engineering Support Organisation</title>
<link rel="stylesheet" href="https://fonts.googleapis.com/css2?family=Orbitron:wght@600;700;800&family=Montserrat:wght@400;500;600;700&display=swap">
<style>
:root{
  --cyan:#1ca9e1;
  --cyan-dark:#1590c4;
  --navy:#1861ab;
  --steel:#85acd3;
  --mist:#d0dfed;
  --pale:#cee9f5;
  --ink:#1b1b1b;
  --grey:#6b6b6b;
  --white:#ffffff;
  --black:#0c0c0c;
  --canvas:#f2f2f2;
}
*{box-sizing:border-box;margin:0;padding:0}
html,body{width:1200px;height:4112px;overflow:hidden;background:var(--canvas)}
body{font-family:"Montserrat",Arial,sans-serif;color:var(--ink);position:relative}
.page{position:absolute;left:200px;top:60px;width:800px;height:3990px;background:var(--white);box-shadow:0 6px 30px rgba(0,0,0,.25);overflow:hidden}
.abs{position:absolute}
.heading{font-family:"Orbitron",Arial,sans-serif;font-weight:700;letter-spacing:2px;text-transform:uppercase}
.rule{display:block;width:40px;height:2px;background:var(--cyan);margin-top:6px}
.btn{display:inline-block;background:var(--cyan);color:var(--white);font-size:9px;font-weight:600;padding:7px 18px;border-radius:2px}
.body-text{font-size:8.5px;line-height:1.6;color:var(--grey)}

/* nav */
.nav{left:0;top:0;width:800px;height:64px;background:var(--white);z-index:3}
.brand{left:40px;top:18px;display:flex;align-items:center;gap:8px}
.brand-mark{width:24px;height:24px;border-radius:50%;background:var(--navy)}
.brand-name{font-weight:700;font-size:13px;color:var(--navy);letter-spacing:1px}
.brand-sub{font-size:6px;color:var(--grey);letter-spacing:.5px}
.nav-links{right:40px;top:22px;display:flex;gap:22px;align-items:center;font-size:9px;font-weight:500}
.nav-links .btn{padding:6px 14px}

/* hero */
.hero{left:0;top:64px;width:800px;height:400px;background:linear-gradient(120deg,#6d8fa6 0%,#c6d7e2 45%,#e8eef2 70%,#9fb8c8 100%)}
.hero-shade{left:0;top:64px;width:800px;height:400px;background:linear-gradient(90deg,rgba(10,40,70,.55),rgba(10,40,70,0) 60%)}
.hero-curve{left:0;top:330px;width:800px;height:140px}
.hero-title{left:50px;top:200px;color:var(--white);font-size:26px;line-height:1.25}
.hero-copy{left:50px;top:318px;width:290px;color:var(--white);font-size:8px;line-height:1.6}
.hero-btns{left:50px;top:362px;display:flex;gap:14px}
.hero-btns .ghost{background:var(--navy)}

/* about */
.about-title{left:70px;top:540px;font-size:22px}
.about-copy{left:70px;top:582px;width:400px}
.about-btn{left:70px;top:690px}
.about-graphic{left:500px;top:520px;width:170px;height:170px;background:linear-gradient(135deg,var(--navy),var(--steel));border-radius:12px}
.about-curve{left:0;top:640px;width:800px;height:160px}

/* process */
.process{left:0;top:760px;width:800px;height:380px;background:var(--pale)}
.process-title{left:0;top:800px;width:800px;text-align:center;font-size:20px}
.process-title .rule{margin:6px auto 0}
.step{top:880px;width:152px;height:190px;background:var(--white);border-radius:4px;box-shadow:4px 6px 0 rgba(24,97,171,.35);text-align:center;padding:22px 14px}
.step .icon{width:30px;height:30px;border-radius:50%;background:var(--cyan);margin:0 auto 10px;display:flex;align-items:center;justify-content:center}
.step h3{font-size:10px;color:var(--ink);margin-bottom:8px}
.step p{font-size:7.5px;line-height:1.55;color:var(--grey)}
.step.active{background:var(--cyan);top:860px;height:210px}
.step.active .icon{background:var(--white)}
.step.active h3,.step.active p{color:var(--white)}

/* services */
.services{left:0;top:1130px;width:800px;height:1600px;background:var(--cyan)}
.services-title{left:0;top:1190px;width:800px;text-align:center;color:var(--white);font-size:20px}
.services-title .rule{margin:6px auto 0;background:var(--white)}
.svc-photo{width:272px;height:236px;border:4px solid var(--white);box-shadow:6px 6px 0 rgba(0,0,0,.15)}
.svc-text{width:300px;color:var(--white)}
.svc-text h3{font-size:15px;font-weight:600}
.svc-text .rule{background:var(--white);margin-bottom:12px}
.svc-text p{font-size:8.5px;line-height:1.6;color:rgba(255,255,255,.9)}

/* reviews */
.reviews-title{left:0;top:2790px;width:800px;text-align:center;font-size:20px}
.reviews-title .rule{margin:6px auto 0}
.review{top:2860px;width:192px;height:240px;background:var(--white);box-shadow:0 3px 12px rgba(0,0,0,.15);overflow:hidden}
.review .quote{position:absolute;left:14px;top:10px;font-family:"Orbitron",Arial,sans-serif;font-size:26px;color:var(--cyan)}
.review p{position:absolute;left:18px;top:44px;width:156px;font-size:7.5px;line-height:1.55;color:var(--grey)}
.review .band{position:absolute;left:0;top:140px;width:192px;height:100px;background:var(--cyan)}
.review .avatar{position:absolute;left:74px;top:112px;width:44px;height:44px;border-radius:50%;border:3px solid var(--white);background:linear-gradient(135deg,#8fa2b0,#d4dde3)}
.review .who{position:absolute;left:0;top:168px;width:192px;text-align:center;color:var(--white);font-size:8px;font-weight:600}
.review .dots{position:absolute;left:0;top:190px;width:192px;display:flex;justify-content:center;gap:6px}
.review .dots span{width:7px;height:7px;border-radius:50%;background:var(--white)}

/* contact */
.contact-photo{left:100px;top:3180px;width:330px;height:380px;background:linear-gradient(135deg,#cfd6dc,#eef1f3 50%,#b9c4cc)}
.contact-panel{left:420px;top:3200px;width:290px;height:340px;background:var(--white);box-shadow:0 3px 14px rgba(0,0,0,.18);padding:22px 26px}
.contact-panel h2{font-size:17px}
.field{height:22px;border:1px solid var(--steel);margin-top:12px;font-size:7.5px;color:var(--grey);padding:6px 8px}
.field.area{height:70px}
.contact-panel .btn{margin-top:14px}
.contact-corner{left:690px;top:3520px;width:20px;height:20px}

/* footer */
.footer{left:0;top:3700px;width:800px;height:290px;background:var(--black);color:var(--white)}
.foot-brand{left:50px;top:3740px}
.foot-brand .brand-name{color:var(--white)}
.foot-about{left:50px;top:3790px;width:190px;font-size:7.5px;line-height:1.6;color:#b9b9b9}
.foot-col{top:3740px}
.foot-col h4{font-size:9px;font-weight:600;margin-bottom:12px}
.foot-col li{list-style:none;font-size:7.5px;color:#b9b9b9;margin-bottom:7px;padding-left:10px;position:relative}
.foot-col li::before{content:"";position:absolute;left:0;top:3px;width:4px;height:4px;background:var(--cyan)}
.social{display:flex;gap:6px;margin-top:4px}
.social span{width:16px;height:16px;border-radius:50%;background:var(--cyan)}
.foot-form{display:flex;margin-top:12px}
.foot-form span{width:70px;height:16px;background:var(--white)}
.foot-form b{width:30px;height:16px;background:var(--cyan)}
.foot-line{left:50px;top:3940px;width:700px;height:1px;background:#333}
.copyright{left:0;top:3956px;width:800px;text-align:center;font-size:7px;color:#9a9a9a}
</style>
</head>
<body>
<div class="page">

  <!-- hero -->
  <div class="abs hero" role="img" aria-label="Photo of laboratory staff in lab coats and hairnets inspecting production samples"></div>
  <div class="abs hero-shade"></div>
  <svg class="abs hero-curve" viewBox="0 0 800 140" preserveAspectRatio="none"><path d="M0 134 Q420 150 800 0 L800 140 L0 140 Z" fill="#ffffff"/></svg>

  <header class="abs nav">
    <div class="abs brand"><span class="brand-mark"></span><div><div class="brand-name">TRIVOLT</div><div class="brand-sub">ENGINEERING</div></div></div>
    <nav class="abs nav-links"><span>Home</span><span>About</span><span>Process</span><span>Services</span><span>Reviews</span><span>Contact</span><span class="btn">Get a Quote</span></nav>
  </header>

  <h1 class="abs heading hero-title">Manufacturing<br>Engineering Support<br>Organisation</h1>
  <p class="abs hero-copy">Reliable engineering, maintenance and reliability support for food, beverage and ingredients manufacturers across every stage of production.</p>
  <div class="abs hero-btns"><span class="btn">Learn More</span><span class="btn ghost">Contact Us</span></div>

  <!-- about -->
  <svg class="abs about-curve" viewBox="0 0 800 160" preserveAspectRatio="none"><path d="M0 120 Q500 140 800 40 L800 160 L0 160 Z" fill="#cee9f5"/></svg>
  <h2 class="abs heading about-title">About Us<span class="rule"></span></h2>
  <p class="abs body-text about-copy">Trivolt Engineering is the maintenance and reliability partner of Corrick &amp; Associates, the design and consultancy group behind many leading food and beverage plants. Together we plan, build and maintain production assets, helping engineering managers reduce downtime, control costs and keep equipment running safely. Our team combines practical site experience with proven systems for planning, execution and continuous improvement.</p>
  <span class="abs btn about-btn">Learn More</span>
  <div class="abs about-graphic" role="img" aria-label="Isometric illustration of stacked engineering blocks"></div>

  <!-- process -->
  <section class="abs process"></section>
  <h2 class="abs heading process-title">Process<span class="rule"></span></h2>
  <div class="abs step" style="left:120px"><div class="icon"><svg width="14" height="14" viewBox="0 0 14 14"><circle cx="7" cy="7" r="5" fill="none" stroke="#fff" stroke-width="2"/></svg></div><h3>Assess</h3><p>We review your site, assets and maintenance data to find the gaps that cost you time and output.</p></div>
  <div class="abs step active" style="left:324px"><div class="icon"><svg width="14" height="14" viewBox="0 0 14 14"><path d="M2 7 L6 11 L12 3" fill="none" stroke="#1ca9e1" stroke-width="2"/></svg></div><h3>Plan</h3><p>We build a clear programme of work with priorities, resources and measurable targets for your team.</p></div>
  <div class="abs step" style="left:528px"><div class="icon"><svg width="14" height="14" viewBox="0 0 14 14"><rect x="3" y="2" width="8" height="10" fill="none" stroke="#fff" stroke-width="2"/></svg></div><h3>Deliver</h3><p>Our engineers carry out the work on site and report results so gains are tracked and sustained.</p></div>

  <!-- services -->
  <section class="abs services"></section>
  <h2 class="abs heading services-title">Our Services<span class="rule"></span></h2>

  <div class="abs svc-photo" style="left:88px;top:1248px;background:linear-gradient(135deg,#9fb6c6,#e4ecf1 55%,#6f8ea3)" role="img" aria-label="Photo of technician in protective clothing using a tablet"></div>
  <div class="abs svc-text" style="left:440px;top:1300px"><h3>Major Equipment</h3><span class="rule"></span><p>Specification, installation and upgrade of process lines, utilities and packaging equipment, managed from concept through to handover with minimal disruption to production.</p></div>

  <div class="abs svc-text" style="left:100px;top:1530px"><h3>Maintenance Management</h3><span class="rule"></span><p>Planned maintenance systems, spare parts strategy and work scheduling that give engineering managers full control of asset condition and cost across the plant.</p></div>
  <div class="abs svc-photo" style="left:428px;top:1492px;background:linear-gradient(135deg,#5f7d95,#c8d4dc 50%,#8a6a55)" role="img" aria-label="Photo of engineers reviewing equipment in a workshop"></div>

  <div class="abs svc-photo" style="left:88px;top:1728px;background:linear-gradient(135deg,#b4bfc6,#eef1f3 45%,#7c8b95)" role="img" aria-label="Photo of stainless steel processing pipework"></div>
  <div class="abs svc-text" style="left:440px;top:1780px"><h3>Maintenance Execution</h3><span class="rule"></span><p>Skilled technicians for breakdown response, shutdowns and routine tasks, working to your procedures and hygiene standards to keep lines safe and productive.</p></div>

  <div class="abs svc-text" style="left:100px;top:2020px"><h3>Manufacturing Performance</h3><span class="rule"></span><p>Root cause analysis, reliability studies and performance tracking that raise equipment effectiveness and turn recurring losses into lasting improvements.</p></div>
  <div class="abs svc-photo" style="left:428px;top:1972px;background:linear-gradient(135deg,#1d3a5a,#3f6d96 50%,#0f1f30)" role="img" aria-label="Photo of gloved hands working on machinery"></div>

  <div class="abs svc-photo" style="left:88px;top:2200px;background:linear-gradient(135deg,#c9d3b8,#eaeee4 45%,#b04a3c)" role="img" aria-label="Photo of worker in protective suit operating filling equipment"></div>
  <div class="abs svc-text" style="left:440px;top:2250px"><h3>Major Equipment</h3><span class="rule"></span><p>Project support for capital investment, from feasibility and vendor selection to factory acceptance, installation checks and operator training on new assets.</p></div>

  <div class="abs svc-text" style="left:100px;top:2490px"><h3>Commissioning</h3><span class="rule"></span><p>Structured testing and validation of new and modified plant, with full documentation so equipment is handed over ready for reliable production from day one.</p></div>
  <div class="abs svc-photo" style="left:428px;top:2440px;background:linear-gradient(135deg,#9ab0c2,#dfe8ef 50%,#4d6a85)" role="img" aria-label="Photo of staff in cleanroom clothing inspecting a production line"></div>

  <!-- reviews -->
  <h2 class="abs heading reviews-title">Reviews<span class="rule"></span></h2>
  <div class="abs review" style="left:80px"><span class="quote">“</span><p>Their planning team cut our unplanned downtime within months. Clear reporting and great people on site.</p><div class="band"></div><div class="avatar" role="img" aria-label="Portrait of reviewer"></div><div class="who">Laura Hensley</div><div class="dots"><span></span><span></span><span></span></div></div>
  <div class="abs review" style="left:304px"><span class="quote">“</span><p>Commissioning of our new line ran on time and the handover documents were the best we have received.</p><div class="band"></div><div class="avatar" role="img" aria-label="Portrait of reviewer"></div><div class="who">Daniel Whitcombe</div><div class="dots"><span></span><span></span><span></span></div></div>
  <div class="abs review" style="left:528px"><span class="quote">“</span><p>A practical, reliable partner who understands food safety and what engineering managers really need.</p><div class="band"></div><div class="avatar" role="img" aria-label="Portrait of reviewer"></div><div class="who">Priya Rendall</div><div class="dots"><span></span><span></span><span></span></div></div>

  <!-- contact -->
  <div class="abs contact-photo" role="img" aria-label="Photo of customer support staff wearing headsets at a laptop"></div>
  <div class="abs contact-panel">
    <h2 class="heading">Contact Us<span class="rule"></span></h2>
    <div class="field">Your Name</div>
    <div class="field">Email Address</div>
    <div class="field">Phone Number</div>
    <div class="field area">Message</div>
    <span class="btn">Submit</span>
  </div>
  <svg class="abs contact-corner" viewBox="0 0 20 20"><path d="M20 0 L20 20 L0 20 Z" fill="#1ca9e1"/></svg>

  <!-- footer -->
  <footer class="abs footer"></footer>
  <div class="abs brand foot-brand"><span class="brand-mark" style="background:var(--cyan)"></span><div><div class="brand-name">TRIVOLT</div><div class="brand-sub" style="color:#b9b9b9">ENGINEERING</div></div></div>
  <p class="abs foot-about">Trivolt Engineering delivers maintenance and reliability services alongside the design and consultancy expertise of Corrick &amp; Associates.</p>
  <div class="abs foot-col" style="left:300px"><h4>Quick Links</h4><ul><li>Home</li><li>About</li><li>Services</li><li>Contact</li></ul></div>
  <div class="abs foot-col" style="left:430px"><h4>Services</h4><ul><li>Process &amp; Control Design</li><li>Major Equipment</li><li>Maintenance Management</li><li>Maintenance Execution</li><li>Manufacturing Performance</li><li>Commissioning</li></ul></div>
  <div class="abs foot-col" style="left:640px"><h4>Follow Us</h4><div class="social"><span></span><span></span><span></span><span></span></div><div class="foot-form"><span></span><b></b></div></div>
  <div class="abs foot-line"></div>
  <p class="abs copyright">© 2024 Trivolt Engineering. All rights reserved.</p>
</div>
</body>
</html>
```